Insurance company needs a business card design

We need a business card design for a Massachusetts-based insurance company Veloria Insurance, LLC. We provide auto insurance to Hispanic (Spanish- or Portuguese-speaking) immigrants in the United States. We will give these business cards to auto dealers where such customers typically go to purchase vehicles. We will provide a solution to the dealers to provide easy insurance to the customers buying cars at their dealerships. Veloria is the Spanish word for protection.
Contact Information for Business Card
Name, Designation, Company Name, Address, Phone Number, Email, Website
Look and feel
Each slider illustrates characteristics of the customer's brand and the style your logo design should communicate.

```html
<!DOCTYPE html>
<html lang="en">
<head>
<meta charset="utf-8">
<title>Veloria Insurance — Business Card</title>
<link rel="stylesheet" href="https://fonts.googleapis.com/css2?family=Montserrat:wght@700&family=Nunito+Sans:wght@400&display=swap">
<style>
  :root {
    --page-bg: #e7e4df;
    --navy: #13294a;
    --navy-deep: #0b1a33;
    --navy-light: #27456e;
    --orange: #d2521a;
    --frost-light: #f3f1ee;
    --frost-mid: #dcdad6;
    --text-light: #e4e8ee;
  }
  * { margin: 0; padding: 0; box-sizing: border-box; }
  html, body { width: 1200px; height: 969px; overflow: hidden; background: var(--page-bg); }
  .card {
    position: absolute; left: 80px; top: 188px;
    width: 1040px; height: 592px;
    border-radius: 26px; overflow: hidden;
    background: linear-gradient(160deg, var(--frost-light), var(--frost-mid));
    box-shadow: 0 12px 40px rgba(0,0,0,0.18);
  }
  .card-shape { position: absolute; inset: 0; width: 100%; height: 100%; }
  .person-name {
    position: absolute; left: 57px; top: 216px;
    font: 700 31px/1 "Montserrat", sans-serif; color: var(--orange); letter-spacing: 0.5px;
  }
  .person-title, .address-line, .contact-line {
    font: 400 22px/1 "Nunito Sans", sans-serif; color: var(--text-light);
  }
  .person-title { position: absolute; left: 57px; top: 250px; }
  .address { position: absolute; left: 59px; top: 318px; }
  .address-line { display: block; height: 29.5px; }
  .contacts { position: absolute; left: 60px; top: 420px; list-style: none; }
  .contact-line { display: flex; align-items: center; height: 30px; }
  .contact-line svg { width: 20px; height: 20px; margin-right: 12px; fill: var(--orange); flex: none; }
  .brand {
    position: absolute; left: 620px; top: 272px;
    display: flex; align-items: center; gap: 14px;
  }
  .brand-square { width: 22px; height: 22px; background: var(--orange); }
  .brand-name {
    font: 700 34px/1 "Montserrat", sans-serif; color: var(--navy); letter-spacing: 1px;
  }
</style>
</head>
<body>
  <div class="card">
    <svg class="card-shape" viewBox="0 0 1230 700" preserveAspectRatio="none" aria-hidden="true">
      <defs>
        <linearGradient id="navyFill" x1="0" y1="0" x2="1" y2="1">
          <stop offset="0" stop-color="var(--navy-light)"/>
          <stop offset="0.6" stop-color="var(--navy)"/>
          <stop offset="1" stop-color="var(--navy-deep)"/>
        </linearGradient>
      </defs>
      <path d="M0 0 H375 C455 260 660 610 1150 700 H0 Z" fill="url(#navyFill)"/>
      <path d="M384 0 C466 262 676 612 1160 700" fill="none" stroke="#ffffff" stroke-width="5"/>
      <path d="M396 0 C480 262 700 600 1160 690" fill="none" stroke="var(--orange)" stroke-width="8"/>
    </svg>

    <div class="person-name">DANIEL REYES</div>
    <div class="person-title">President</div>

    <address class="address" style="font-style:normal">
      <span class="address-line">4129 Willow Crest Lane</span>
      <span class="address-line">Worcester</span>
      <span class="address-line">Massachusetts 01604</span>
    </address>

    <ul class="contacts">
      <li class="contact-line">
        <svg viewBox="0 0 24 24"><path d="M6.6 10.8a15 15 0 0 0 6.6 6.6l2.2-2.2c.3-.3.7-.4 1-.2 1.1.4 2.3.6 3.6.6.6 0 1 .4 1 1V20c0 .6-.4 1-1 1A17 17 0 0 1 3 4c0-.6.4-1 1-1h3.5c.6 0 1 .4 1 1 0 1.3.2 2.5.6 3.6.1.3 0 .7-.2 1z"/></svg>
        508-555-0142
      </li>
      <li class="contact-line">
        <svg viewBox="0 0 24 24"><path d="M7 1h10a2 2 0 0 1 2 2v18a2 2 0 0 1-2 2H7a2 2 0 0 1-2-2V3a2 2 0 0 1 2-2zm0 3v14h10V4zm5 15.5a1 1 0 1 0 0 2 1 1 0 0 0 0-2z"/></svg>
        508-555-0187
      </li>
      <li class="contact-line">
        <svg viewBox="0 0 24 24"><path d="M2 5h20v14H2zm2 2v.5l8 5 8-5V7zm0 2.8V17h16V9.8l-8 5z"/></svg>
        info@veloriainsurance.com
      </li>
      <li class="contact-line">
        <svg viewBox="0 0 24 24"><path d="M12 2a10 10 0 1 0 0 20 10 10 0 0 0 0-20zm-1 17.9A8 8 0 0 1 4.2 10.2L9 15v1a2 2 0 0 0 2 2zm6.9-2.5A2 2 0 0 0 16 16h-1v-3a1 1 0 0 0-1-1H8v-2h2a1 1 0 0 0 1-1V7h2a2 2 0 0 0 2-2v-.4a8 8 0 0 1 2.9 12.8z"/></svg>
        veloriainsurance.com
      </li>
    </ul>

    <div class="brand">
      <span class="brand-square"></span>
      <span class="brand-name">VELORIA INSURANCE</span>
    </div>
  </div>
</body>
</html>
```